International Automotive Parts Marketing business needs professional, sleek Android app design.

We have developed an Android app for our sales team and are now looking for an overall design our developers can apply. The design should mirror our corporate website kvrelo.com. There is a LOT of data the reps need to work through so not really any images other that login screen - of course icons are great. Lots of lists and searches etc. - it needs to look professional, feel amazing and easy to use. Our motto - Simple is always better. We included our logo and a few screenshots of the app page 1 and 2.

Target Market(s)

Professional Sales and Marketing - our own sales team (100 reps) will use this app

Font styles to use
Sans Serif

Colors

Designer to choose colors to be used in the design.

Requirements
Must have
• App design must be professional and easy to use in the field all day. Similar look and feel of corporate website kvrelo.com. Same colors and images. Icons to manage navigation
Should not have
• Non-professional look and feel. No vector cartoon type images. No specific parts related images

```html
<!DOCTYPE html>
<html lang="en">
<head>
<meta charset="utf-8">
<title>Kvrelo Parts – Sales App UI</title>
<link rel="stylesheet" href="https://fonts.googleapis.com/css2?family=Roboto:wght@300;400;500&display=swap">
<style>
:root{
  --red:#d5002b;
  --red-soft:#fde8ec;
  --black:#000;
  --ink:#222;
  --muted:#9a9a9a;
  --line:#e8e8ea;
  --canvas:#f4f5f7;
  --panel:#f6f6f8;
  --white:#fff;
}
*{box-sizing:border-box;margin:0;padding:0}
html,body{width:1200px;height:4272px;overflow:hidden}
body{background:var(--canvas);font-family:"Roboto",sans-serif;color:var(--ink);position:relative}
.abs{position:absolute}
.screen{position:absolute;width:316px;background:var(--white);box-shadow:0 6px 24px rgba(0,0,0,.06);overflow:hidden}
.statusbar{position:absolute;left:0;top:0;width:100%;height:16px;background:#4a4a4a}
.appbar{position:absolute;left:0;top:16px;width:100%;height:45px;background:var(--black);color:#fff;font-size:13px;display:flex;align-items:center;justify-content:center}
.appbar .lead{position:absolute;left:14px;top:13px}
.appbar .gear{position:absolute;right:14px;top:13px}
.filters{position:absolute;left:0;top:61px;width:100%;height:51px;display:flex;border-bottom:1px solid var(--line)}
.filters div{flex:1;padding:9px 14px;border-right:1px solid var(--line)}
.filters div:last-child{border-right:0}
.label{font-size:9.5px;color:var(--muted);display:block}
.value{font-size:12px;color:var(--ink);display:block;margin-top:6px}
.filters .value{color:var(--red)}
.searchzone{position:absolute;left:0;width:100%;background:var(--panel)}
.searchbox{position:absolute;left:14px;right:14px;height:40px;background:#fff;border:1px solid var(--line);display:flex;align-items:center}
.searchbox .q{margin:0 8px 0 12px}
.searchbox .ph{font-size:9.5px;color:var(--muted);flex:1}
.searchbox .txt{font-size:10px;color:var(--ink);flex:1}
.searchbox .tune{width:40px;height:100%;border-left:1px solid var(--line);display:flex;align-items:center;justify-content:center}
.btn{position:absolute;left:14px;right:14px;height:38px;display:flex;align-items:center;justify-content:center;font-size:13px}
.btn.primary{background:var(--red);color:#fff}
.btn.outline{border:1px solid #d9d9dc;color:var(--red);background:#fff}
.tabbar{position:absolute;left:0;bottom:0;width:100%;height:66px;display:flex;justify-content:space-around;align-items:center;padding:0 6px;background:#fff}
.tabbar span{width:36px;height:36px;display:flex;align-items:center;justify-content:center;border-radius:4px}
.tabbar span.active{background:var(--red-soft)}
.tabbar svg{width:20px;height:20px}
.wordmark{display:flex;align-items:center;gap:10px;font-weight:500;color:var(--black);letter-spacing:.5px}
.wordmark .dot{border-radius:50%;background:var(--red)}
.field{position:absolute;left:0;right:0;padding:0 14px}
.field .value{margin-top:5px;font-size:11.5px}
.rule{position:absolute;height:1px;background:var(--line)}
.panel{position:absolute;left:14px;right:14px;border:1px solid var(--line);background:#fff}
.section{position:absolute;left:14px;font-size:12.5px;color:var(--ink)}
.card{position:absolute;left:14px;right:14px;height:73px;border:1px solid var(--line);background:#fff;padding:7px 8px}
.card .name{font-size:12px;color:var(--ink)}
.card .city{font-size:10px;color:var(--red);margin-top:5px}
.card .meta{position:absolute;left:8px;right:8px;bottom:8px;display:flex;gap:22px;font-size:8.5px;color:var(--muted)}
.card .meta b{font-weight:400;color:var(--ink)}
.card .mark{position:absolute;right:8px;top:8px;width:26px;height:26px;border-radius:50%;background:var(--red)}
.menu-item{position:absolute;left:14px;width:230px;height:45px;display:flex;align-items:center;gap:14px;font-size:12.5px;border-bottom:1px solid var(--line)}
.check{width:20px;height:20px;border:1.5px solid #c8c8cc;border-radius:4px;display:inline-flex;align-items:center;justify-content:center;vertical-align:middle}
.check.on{background:var(--red);border-color:var(--red)}
.checkrow{font-size:11px;color:var(--muted);display:flex;align-items:center;gap:8px}
</style>
</head>
<body>

<svg width="0" height="0" style="position:absolute">
  <defs>
    <symbol id="i-search" viewBox="0 0 20 20"><circle cx="8.5" cy="8.5" r="6" fill="none" stroke="currentColor" stroke-width="2"/><path d="M13 13l5 5" stroke="currentColor" stroke-width="2.2" stroke-linecap="round"/></symbol>
    <symbol id="i-route" viewBox="0 0 20 20"><circle cx="5" cy="5" r="3.2" fill="currentColor"/><path d="M5 9v2c0 3 10 0 10 4" fill="none" stroke="currentColor" stroke-width="1.6"/><circle cx="15" cy="16" r="2.4" fill="currentColor"/><path d="M13 5h5M13 8h3" stroke="currentColor" stroke-width="1.5"/></symbol>
    <symbol id="i-list" viewBox="0 0 20 20"><g fill="currentColor"><rect x="2" y="4" width="2.2" height="2.2"/><rect x="2" y="9" width="2.2" height="2.2"/><rect x="2" y="14" width="2.2" height="2.2"/><rect x="6.5" y="4.3" width="11" height="1.6"/><rect x="6.5" y="9.3" width="11" height="1.6"/><rect x="6.5" y="14.3" width="11" height="1.6"/></g></symbol>
    <symbol id="i-partner" viewBox="0 0 20 20"><g fill="currentColor"><circle cx="7" cy="6" r="3.2"/><path d="M1.5 17c0-4 2.5-6.5 5.5-6.5s5.5 2.5 5.5 6.5z"/><circle cx="13.5" cy="5" r="2.8"/><path d="M11 10c1-.8 1.8-1 2.5-1 3 0 5 2.3 5 6.5h-4.5c0-2.5-1-4.3-3-5.5z"/></g></symbol>
    <symbol id="i-touch" viewBox="0 0 20 20"><g fill="currentColor"><circle cx="10" cy="5" r="2.6"/><path d="M6.5 12c0-2.3 1.6-4 3.5-4s3.5 1.7 3.5 4z"/><path d="M1.5 17.5l2-4h1.6l-1.4 2.8h12.6l-1.4-2.8h1.6l2 4z"/></g></symbol>
    <symbol id="i-gear" viewBox="0 0 20 20"><circle cx="10" cy="10" r="6.2" fill="none" stroke="currentColor" stroke-width="3.4" stroke-dasharray="2.6 2.3"/><circle cx="10" cy="10" r="5" fill="currentColor"/><circle cx="10" cy="10" r="2" fill="#000"/></symbol>
    <symbol id="i-tune" viewBox="0 0 20 20"><g stroke="currentColor" stroke-width="1.3" fill="none"><path d="M3 5h14M3 10h14M3 15h14"/><circle cx="7" cy="5" r="1.6" fill="#fff"/><circle cx="13" cy="10" r="1.6" fill="#fff"/><circle cx="8" cy="15" r="1.6" fill="#fff"/></g></symbol>
    <symbol id="i-menu" viewBox="0 0 20 20"><path d="M1 4h18M1 10h18M1 16h18" stroke="currentColor" stroke-width="1.6"/></symbol>
    <symbol id="i-back" viewBox="0 0 20 20"><path d="M13 3l-7 7 7 7" fill="none" stroke="currentColor" stroke-width="2"/></symbol>
    <symbol id="i-user" viewBox="0 0 20 20"><circle cx="10" cy="6.5" r="4" fill="none" stroke="currentColor" stroke-width="1.4"/><path d="M2.5 18c0-4.5 3.4-6.5 7.5-6.5s7.5 2 7.5 6.5z" fill="none" stroke="currentColor" stroke-width="1.4"/></symbol>
    <symbol id="i-lock" viewBox="0 0 20 20"><rect x="3.5" y="8.5" width="13" height="10" fill="none" stroke="currentColor" stroke-width="1.4"/><path d="M6.5 8.5V6a3.5 3.5 0 017 0v2.5" fill="none" stroke="currentColor" stroke-width="1.4"/></symbol>
    <symbol id="i-cal" viewBox="0 0 20 20"><rect x="2" y="4" width="16" height="14" rx="1.5" fill="currentColor"/><rect x="5" y="1.5" width="2" height="4" fill="currentColor"/><rect x="13" y="1.5" width="2" height="4" fill="currentColor"/><path d="M2 8h16" stroke="#fff" stroke-width="1.2"/></symbol>
    <symbol id="i-tick" viewBox="0 0 20 20"><path d="M4 10.5l4 4 8-9" fill="none" stroke="#fff" stroke-width="2.4"/></symbol>
    <symbol id="i-edit" viewBox="0 0 20 20"><path d="M3 17h4l10-10-4-4L3 13z" fill="none" stroke="currentColor" stroke-width="1.6"/></symbol>
  </defs>
</svg>

<!-- Login -->
<section class="screen" style="left:136px;top:61px;height:562px">
  <div class="wordmark abs" style="left:64px;top:96px;font-size:17px"><span class="dot" style="width:40px;height:40px"></span>KVRELO PARTS</div>
  <div class="abs" style="left:28px;top:205px;width:260px">
    <span class="label">Username</span>
    <span class="value" style="font-size:13px;margin-top:8px">user@kvrelo.com</span>
    <svg class="abs" style="right:0;top:12px;width:18px;height:18px;color:var(--red)"><use href="#i-user"/></svg>
  </div>
  <div class="rule" style="left:28px;top:249px;width:260px;background:#dcdcdf"></div>
  <div class="abs" style="left:28px;top:283px;width:260px">
    <span class="label">Password</span>
    <span class="value" style="font-size:12px;margin-top:7px;letter-spacing:2px">*******</span>
    <svg class="abs" style="right:0;top:13px;width:18px;height:18px;color:var(--red)"><use href="#i-lock"/></svg>
  </div>
  <div class="rule" style="left:28px;top:326px;width:260px;background:#dcdcdf"></div>
  <div class="abs" style="right:28px;top:356px;font-size:12.5px;color:var(--red)">Forgot Password ?</div>
  <div class="btn primary" style="left:28px;right:28px;top:429px;height:40px">Log In</div>
</section>

<!-- Brand sheet -->
<div class="wordmark abs" style="left:704px;top:75px;font-size:26px;gap:14px"><span class="dot" style="width:64px;height:64px"></span>KVRELO PARTS</div>
<div class="abs" style="left:703px;top:177px;font-size:17px;color:#444">Fonts</div>
<div class="abs" style="left:703px;top:206px;font-size:17px;color:#444;display:flex;gap:18px">
  <span>Roboto - Regular</span><span style="font-weight:500;color:#222">Medium</span><span style="font-weight:300;color:#888">Light</span>
</div>
<div class="abs" style="left:703px;top:263px;font-size:17px;color:#444">Colors</div>
<div class="abs" style="left:703px;top:298px;display:flex;gap:16px">
  <span style="width:50px;height:50px;background:#fff;display:flex;align-items:center;justify-content:center"><span style="width:30px;height:28px;background:var(--red)"></span></span>
  <span style="width:50px;height:50px;background:#fff;display:flex;align-items:center;justify-content:center"><span style="width:30px;height:28px;background:var(--black)"></span></span>
  <span style="width:50px;height:50px;background:#fff;display:flex;align-items:center;justify-content:center"><span style="width:30px;height:28px;background:#f4f4f6"></span></span>
</div>

<!-- Search empty -->
<section class="screen" style="left:727px;top:517px;height:562px">
  <div class="statusbar"></div>
  <header class="appbar"><svg class="lead" style="width:20px;height:20px;color:#fff"><use href="#i-menu"/></svg>Search<svg class="gear" style="width:20px;height:20px;color:#fff"><use href="#i-gear"/></svg></header>
  <div class="filters"><div><span class="label">Type</span><span class="value">AB+M</span></div><div><span class="label">Rating</span><span class="value">All</span></div></div>
  <div class="searchzone" style="top:112px;height:52px"></div>
  <div class="searchbox" style="top:118px"><svg class="q" style="width:18px;height:18px;color:var(--red)"><use href="#i-search"/></svg><span class="ph">Please enter here</span><span class="tune"><svg style="width:16px;height:16px;color:#888"><use href="#i-tune"/></svg></span></div>
  <div class="btn outline" style="top:386px">Advance Search</div>
  <div class="btn primary" style="top:440px">Search</div>
  <nav class="tabbar">
    <span><svg style="color:#333"><use href="#i-route"/></svg></span>
    <span class="active"><svg style="color:var(--red)"><use href="#i-search"/></svg></span>
    <span><svg style="color:#333"><use href="#i-list"/></svg></span>
    <span><svg style="color:#333"><use href="#i-partner"/></svg></span>
    <span><svg style="color:#333"><use href="#i-touch"/></svg></span>
  </nav>
</section>

<!-- Search suggestions -->
<section class="screen" style="left:136px;top:971px;height:562px">
  <div class="statusbar"></div>
  <header class="appbar"><svg class="lead" style="width:20px;height:20px;color:#fff"><use href="#i-menu"/></svg>Search<svg class="gear" style="width:20px;height:20px;color:#fff"><use href="#i-gear"/></svg></header>
  <div class="filters"><div><span class="label">Type</span><span class="value">AB+M</span></div><div><span class="label">Rating</span><span class="value">All</span></div></div>
  <div class="searchzone" style="top:112px;height:52px"></div>
  <div class="searchbox" style="top:118px"><svg class="q" style="width:18px;height:18px;color:var(--red)"><use href="#i-search"/></svg><span class="txt">Auto|</span><span class="tune"><svg style="width:16px;height:16px;color:#888"><use href="#i-tune"/></svg></span></div>
  <div class="abs" style="left:14px;right:14px;top:166px;background:#fff;box-shadow:0 3px 8px rgba(0,0,0,.08);font-size:10px">
    <div style="height:42px;padding:0 14px;display:flex;align-items:center;border-bottom:1px solid var(--line)">Auto Care Depot</div>
    <div style="height:42px;padding:0 14px;display:flex;align-items:center;border-bottom:1px solid var(--line)">Auto Hub Supply</div>
    <div style="height:42px;padding:0 14px;display:flex;align-items:center">Pinecrest Automotive</div>
  </div>
  <div class="btn outline" style="top:386px">Advance Search</div>
  <div class="btn primary" style="top:440px">Search</div>
  <nav class="tabbar">
    <span><svg style="color:#333"><use href="#i-route"/></svg></span>
    <span class="active"><svg style="color:var(--red)"><use href="#i-search"/></svg></span>
    <span><svg style="color:#333"><use href="#i-list"/></svg></span>
    <span><svg style="color:#333"><use href="#i-partner"/></svg></span>
    <span><svg style="color:#333"><use href="#i-touch"/></svg></span>
  </nav>
</section>

<!-- Navigation drawer -->
<section class="screen" style="left:727px;top:1640px;height:562px">
  <div class="abs" style="right:0;top:0;width:58px;height:100%;background:#7b7b7b">
    <div style="height:16px;background:#2e2e2e"></div>
    <div style="height:45px;background:#111;position:relative"><svg style="position:absolute;left:24px;top:13px;width:20px;height:20px;color:#888"><use href="#i-gear"/></svg></div>
    <svg class="abs" style="left:14px;top:133px;width:16px;height:16px;color:#555"><use href="#i-tune"/></svg>
    <div class="abs" style="left:0;right:14px;top:388px;height:38px;border:1px solid #8e8e8e;background:#808080"></div>
    <div class="abs" style="left:0;right:14px;top:442px;height:38px;background:#6b0016"></div>
    <svg class="abs" style="left:20px;top:517px;width:20px;height:20px;color:#333"><use href="#i-touch"/></svg>
  </div>
  <div class="abs" role="img" aria-label="User profile photo" style="left:99px;top:40px;width:42px;height:42px;border-radius:50%;background:linear-gradient(160deg,#b9a89a,#5d5148)"></div>
  <div class="abs" style="left:0;width:258px;top:96px;text-align:center;font-size:12.5px;font-weight:500">User Name</div>
  <div class="abs" style="left:0;width:258px;top:116px;text-align:center;font-size:10.5px;color:#666">Designation</div>
  <div class="menu-item" style="top:178px"><svg style="width:18px;height:18px;color:var(--red)"><use href="#i-route"/></svg>Route</div>
  <div class="menu-item" style="top:223px"><svg style="width:18px;height:18px;color:var(--red)"><use href="#i-search"/></svg>Search</div>
  <div class="menu-item" style="top:268px"><svg style="width:18px;height:18px;color:var(--red)"><use href="#i-list"/></svg>Custom list</div>
  <div class="menu-item" style="top:313px"><svg style="width:18px;height:18px;color:var(--red)"><use href="#i-partner"/></svg>Partner</div>
  <div class="menu-item" style="top:358px"><svg style="width:18px;height:18px;color:var(--red)"><use href="#i-touch"/></svg>Market Touches</div>
  <div class="menu-item" style="top:403px"><svg style="width:18px;height:18px;color:var(--red)"><use href="#i-gear"/></svg>Accounts</div>
</section>

<!-- Advanced search -->
<section class="screen" style="left:129px;top:2096px;height:747px">
  <div class="statusbar"></div>
  <header class="appbar"><svg class="lead" style="width:20px;height:20px;color:#fff"><use href="#i-menu"/></svg>Search<svg class="gear" style="width:20px;height:20px;color:#fff"><use href="#i-gear"/></svg></header>
  <div class="filters"><div><span class="label">Type</span><span class="value">AB+M</span></div><div><span class="label">Rating</span><span class="value">All</span></div></div>
  <div class="searchzone" style="top:112px;height:62px"></div>
  <div class="searchbox" style="top:124px"><svg class="q" style="width:18px;height:18px;color:var(--red)"><use href="#i-search"/></svg><span class="ph">Please enter here</span><span class="tune"><svg style="width:16px;height:16px;color:#888"><use href="#i-tune"/></svg></span></div>
  <div class="section" style="top:188px">Advance Search</div>
  <div class="abs" style="right:14px;top:186px;padding:3px 8px;background:var(--red-soft);color:var(--red);font-size:11px;border-radius:3px">Cancel</div>
  <div class="panel" style="top:216px;height:392px">
    <div class="field" style="top:18px"><span class="label">Market</span><span class="value">All</span></div>
    <div class="rule" style="left:14px;right:14px;top:58px"></div>
    <div class="field" style="top:75px"><span class="label">Franchise</span><span class="value">All</span></div>
    <div class="rule" style="left:14px;right:14px;top:115px"></div>
    <div class="field" style="top:132px"><span class="label">LOI</span><span class="value">None</span></div>
    <div class="rule" style="left:14px;right:14px;top:172px"></div>
    <div class="field checkrow" style="top:187px"><span class="check"></span>Rewards<span style="width:48px"></span><span class="check on"><svg style="width:14px;height:14px"><use href="#i-tick"/></svg></span>My Touches</div>
    <div class="field" style="top:226px"><span class="label">Touch Start</span><span class="value">06/07/2019</span><svg class="abs" style="right:14px;top:12px;width:16px;height:16px;color:#333"><use href="#i-cal"/></svg></div>
    <div class="rule" style="left:14px;right:14px;top:266px"></div>
    <div class="field" style="top:284px"><span class="label">Touch End</span><span class="value">06/09/2019</span><svg class="abs" style="right:14px;top:12px;width:16px;height:16px;color:#333"><use href="#i-cal"/></svg></div>
    <div class="rule" style="left:14px;right:14px;top:324px"></div>
    <div class="field" style="top:341px"><span class="label">Sale Type</span><span class="value">None</span></div>
  </div>
  <div class="btn primary" style="top:627px;height:39px">Search</div>
  <nav class="tabbar" style="height:70px">
    <span><svg style="color:#333"><use href="#i-route"/></svg></span>
    <span class="active"><svg style="color:var(--red)"><use href="#i-search"/></svg></span>
    <span><svg style="color:#333"><use href="#i-list"/></svg></span>
    <span><svg style="color:#333"><use href="#i-partner"/></svg></span>
    <span><svg style="color:#333"><use href="#i-touch"/></svg></span>
  </nav>
</section>

<!-- Results -->
<section class="screen" style="left:727px;top:2949px;height:564px;background:var(--panel)">
  <div class="statusbar"></div>
  <header class="appbar"><svg class="lead" style="width:20px;height:20px;color:#fff"><use href="#i-back"/></svg>Search<svg class="gear" style="width:20px;height:20px;color:#fff"><use href="#i-gear"/></svg></header>
  <div class="searchbox" style="top:72px"><svg class="q" style="width:18px;height:18px;color:#777"><use href="#i-search"/></svg><span class="txt">Auto</span><span class="tune"><svg style="width:16px;height:16px;color:var(--red)"><use href="#i-tune"/></svg></span></div>
  <div class="filters" style="top:121px;height:53px;background:#fff"><div><span class="label">Group By</span><span class="value" style="color:var(--ink)">None</span></div><div><span class="label">Sort By</span><span class="value" style="color:var(--ink)">None</span></div></div>
  <div class="abs" style="left:14px;top:183px;font-size:10px;color:var(--muted)">22 Matches Found</div>
  <div class="card" style="top:204px"><div class="name">Northgate Auto Care</div><div class="city">Brookvale BC</div><span class="mark"></span><div class="meta"><span>Type : <b>M</b></span><span>Rating : <b>B</b></span><span>Last Touch : <b>07/06/2019</b></span></div></div>
  <div class="card" style="top:292px"><div class="name">Firstline Motor Works</div><div class="city">Marlow Bay</div><div class="meta"><span>Type : <b>M</b></span><span>Rating : <b>B</b></span><span>Last Touch : <b>07/06/2019</b></span></div></div>
  <div class="card" style="top:380px"><div class="name">Redwood Collision</div><div class="city">Elmfield BC</div><div class="meta"><span>Type : <b>M</b></span><span>Rating : <b>B</b></span><span>Last Touch : <b>07/06/2019</b></span></div></div>
  <div class="card" style="top:468px"><div class="name">Northgate Auto Care</div></div>
  <nav class="tabbar" style="height:71px">
    <span><svg style="color:#333"><use href="#i-route"/></svg></span>
    <span class="active"><svg style="color:var(--red)"><use href="#i-search"/></svg></span>
    <span><svg style="color:#333"><use href="#i-list"/></svg></span>
    <span><svg style="color:#333"><use href="#i-partner"/></svg></span>
    <span><svg style="color:#333"><use href="#i-touch"/></svg></span>
  </nav>
</section>

<!-- Account detail -->
<section class="screen" style="left:129px;top:3163px;height:1012px">
  <div class="statusbar"></div>
  <header class="appbar"><svg class="lead" style="width:20px;height:20px;color:#fff"><use href="#i-back"/></svg>Search<svg class="gear" style="width:20px;height:20px;color:#fff"><use href="#i-gear"/></svg></header>
  <div class="panel" style="top:76px;height:128px;text-align:center">
    <div style="margin-top:28px;font-size:12.5px">Northgate Auto Care</div>
    <div style="margin-top:7px;font-size:10.5px;color:var(--red)">Brookvale BC</div>
    <div style="margin:9px auto 0;width:62px;height:20px;background:var(--red-soft);color:var(--red);font-size:10px;display:flex;align-items:center;justify-content:center;gap:5px"><svg style="width:11px;height:11px"><use href="#i-edit"/></svg>Edit</div>
  </div>
  <div class="section" style="top:217px">Communication</div>
  <div class="panel" style="top:239px;height:296px">
    <div class="field" style="top:14px"><span class="label">Address 01</span><span class="value">412 B Harbour Lane</span></div>
    <div class="rule" style="left:14px;right:14px;top:54px"></div>
    <div class="field" style="top:72px"><span class="label">Address 02</span></div>
    <div class="rule" style="left:14px;right:14px;top:112px"></div>
    <div class="field" style="top:128px"><span class="label">Phone</span><span class="value">555 0142 386</span></div>
    <div class="rule" style="left:14px;right:14px;top:168px"></div>
    <div class="field" style="top:185px"><span class="label">Fax</span><span class="value">555 0142 386</span></div>
    <div class="rule" style="left:14px;right:14px;top:225px"></div>
    <div class="field" style="top:242px"><span class="label">Email</span><span class="value">info@northgateauto.com</span></div>
  </div>
  <div class="section" style="top:553px">Other Details</div>
  <div class="panel" style="top:575px;height:285px">
    <div class="field" style="top:16px"><span class="label">Type</span><span class="value">M</span></div>
    <div class="rule" style="left:14px;right:14px;top:56px"></div>
    <div class="field" style="top:73px"><span class="label">Rating</span><span class="value">B</span></div>
    <div class="rule" style="left:14px;right:14px;top:113px"></div>
    <div class="field" style="top:130px"><span class="label">Comments</span></div>
    <div class="rule" style="left:14px;right:14px;top:170px"></div>
    <div class="field" style="top:186px"><span class="label">Partner</span><span class="value">Certified Premium Repair</span></div>
    <div class="rule" style="left:14px;right:14px;top:226px"></div>
    <div class="field" style="top:244px"><span class="label">Franchise</span></div>
  </div>
  <div class="btn outline" style="top:890px">Modify List</div>
  <nav class="tabbar" style="height:66px">
    <span><svg style="color:#333"><use href="#i-route"/></svg></span>
    <span class="active"><svg style="color:var(--red)"><use href="#i-search"/></svg></span>
    <span><svg style="color:#333"><use href="#i-list"/></svg></span>
    <span><svg style="color:#333"><use href="#i-partner"/></svg></span>
    <span><svg style="color:#333"><use href="#i-touch"/></svg></span>
  </nav>
</section>

</body>
</html>
```